Business Card for Bloom Vitality & Strength

Hi can you please design a business card with my logo and program logo (the new one I just sent) somewhere on it too maybe on the back? Needs to be eye catching and super cool.
Marla Quintby, Director
Master Personal Trainer & Nutrition Coach
0412 786 305
Www.bloomvitalitystrength.com.au
Insta (logo) bloom_vitality_strength #bloomyou7x72018

Target Market(s)

30+ women looking to change lifestyle to healthy mind body etc

Industry/Entity Type

Health And Wellness

Contact Information for Business Card

As above

Font styles to use
Sans Serif

Colors

Designer to choose colors to be used in the design.

Requirements
Must have
• Must super cool and edgy with a bit of cuteness

```html
<!DOCTYPE html>
<html lang="en">
<head>
<meta charset="utf-8">
<title>Bloom Vitality &amp; Strength — Business Card</title>
<link href="https://fonts.googleapis.com/css2?family=Roboto:wght@400;500;700&family=Tinos:ital,wght@1,700&display=swap" rel="stylesheet">
<style>
  :root {
    --backdrop: #ece8e2;
    --card-light: #f6f6f5;
    --card-dark: #1b1c1e;
    --red: #d0191e;
    --green: #2fb27a;
    --ink: #4f4f4f;
    --ink-dark: #1d1d1d;
    --rule: #6e6e6e;
    --white: #ffffff;
  }
  * { box-sizing: border-box; margin: 0; padding: 0; }
  html, body { width: 1200px; height: 960px; overflow: hidden; }
  body {
    position: relative;
    background: var(--backdrop);
    font-family: "Roboto", Arial, sans-serif;
  }
  .card {
    position: absolute;
    width: 600px;
    height: 344px;
    box-shadow: 0 2px 6px rgba(0,0,0,0.25);
    overflow: hidden;
  }
  .card--front { left: 314px; top: 113px; background: var(--card-light); }
  .card--back  { left: 311px; top: 472px; background: var(--card-dark); }

  .holder-name {
    position: absolute; left: 36px; top: 43px;
    font-size: 21px; font-weight: 700; color: var(--red);
    letter-spacing: -0.2px;
  }
  .holder-roles {
    position: absolute; left: 36px; top: 73px;
    list-style: none;
    font-size: 15px; font-weight: 500; color: var(--green); line-height: 19.5px;
  }
  .contact-list {
    position: absolute; left: 38px; top: 149px;
    list-style: none;
    font-size: 14.5px; color: var(--ink); line-height: 19.5px;
  }
  .contact-list li { display: flex; align-items: center; gap: 8px; }
  .contact-icon { width: 15px; height: 15px; flex: none; }
  .contact-dot { width: 11px; height: 11px; margin: 0 2px; background: var(--red); border-radius: 2px; flex: none; }
  .contact-dot--round { border-radius: 50%; }

  .rule {
    position: absolute; left: 0; width: 566px; height: 2px; background: var(--rule);
  }
  .rule--top { top: 232px; }
  .rule--bottom { top: 285px; }

  .web-front {
    position: absolute; left: 36px; top: 248px;
    font-family: "Tinos", "Times New Roman", serif;
    font-style: italic; font-weight: 700;
    font-size: 16px; color: var(--ink-dark);
  }
  .program-mark {
    position: absolute; right: 44px; top: 246px;
    display: flex; align-items: center; gap: 8px;
  }
  .program-mark__dot { width: 14px; height: 14px; border-radius: 50%; background: var(--red); flex: none; }
  .program-mark__name {
    font-family: "Roboto", Arial, sans-serif; font-weight: 500;
    font-size: 22px; color: var(--ink-dark);
  }

  .back-mark {
    position: absolute; left: 0; right: 0; top: 128px;
    display: flex; justify-content: center; align-items: center; gap: 12px;
  }
  .back-mark__dot { width: 22px; height: 22px; border-radius: 50%; background: var(--red); flex: none; }
  .back-mark__name {
    font-family: "Roboto", Arial, sans-serif; font-weight: 500;
    font-size: 34px; color: var(--red);
  }
  .web-back {
    position: absolute; left: 0; right: 0; top: 284px;
    text-align: center;
    font-size: 14.5px; letter-spacing: 2.2px; color: var(--white);
  }
</style>
</head>
<body>
  <section class="card card--front" aria-label="Card front">
    <h1 class="holder-name">MARLA QUINTBY</h1>
    <ul class="holder-roles">
      <li>Director</li>
      <li>Master Personal Trainer &amp;</li>
      <li>Nutrition Coach</li>
    </ul>
    <ul class="contact-list">
      <li>
        <svg class="contact-icon" viewBox="0 0 24 24" aria-hidden="true">
          <path fill="#d0191e" d="M6.6 10.8a15.1 15.1 0 0 0 6.6 6.6l2.2-2.2c.3-.3.7-.4 1-.2 1.1.4 2.3.6 3.6.6.6 0 1 .4 1 1V20c0 .6-.4 1-1 1A17 17 0 0 1 3 4c0-.6.4-1 1-1h3.5c.6 0 1 .4 1 1 0 1.3.2 2.5.6 3.6.1.3 0 .7-.2 1z"/>
        </svg>
        <span>0412 786 305</span>
      </li>
      <li><span class="contact-dot" aria-hidden="true"></span><span>bloom_vitality_strength</span></li>
      <li><span class="contact-dot contact-dot--round" aria-hidden="true"></span><span>#bloomyou7x72018</span></li>
    </ul>
    <div class="rule rule--top"></div>
    <p class="web-front">www.bloomvitalitystrength.com.au</p>
    <div class="program-mark">
      <span class="program-mark__dot" aria-hidden="true"></span>
      <span class="program-mark__name">Peak Rise Method</span>
    </div>
    <div class="rule rule--bottom"></div>
  </section>

  <section class="card card--back" aria-label="Card back">
    <div class="back-mark">
      <span class="back-mark__dot" aria-hidden="true"></span>
      <span class="back-mark__name">Bloom Vitality &amp; Strength</span>
    </div>
    <p class="web-back">www.bloomvitalitystrength.com.au</p>
  </section>
</body>
</html>
```